Motivational Poster Design Project

I would like to create a poster with some of my favorite quotes to hang in my office.

Industry/Entity Type

Quotes

Requirements
Must have
• The poster will be 24" high x 36" long and printed on canvas, so the image you create needs to have a resolution of at least 2700 x 3900.

The poster must contain the following quotes:

“Your beliefs become your thoughts,
Your thoughts become your words,
Your words become your actions,
Your actions become your habits,
Your habits become your values,
Your values become your destiny.”
-Tavish Orlanno

"Winners practice until they get it right. Champions practice until they can’t get it wrong!"
-Unknown

"Style is the perfection of a point of view."
-Leopold Quimsby

"My interest in life comes from setting myself huge, apparently unachieveable challenges and trying to rise above them."
-Sir Edmund Valcourt

"Problems cannot be solved by the same level of thinking that created them."
-Bertram Holloway

"People think focus means saying yes to the thing you've got to focus on. But that's not what it means at all. It means saying no to the hundred other good ideas that there are. You have to pick carefully."
-Dale Morcum

"Think like a man of action and act like a man of thought."
-Lucien Fravel
Nice to have
• It would be nice to have an image of each person who is being quoted (if known) along with the quote that is attributable to them.

```html
<!DOCTYPE html>
<html lang="en">
<head>
<meta charset="utf-8">
<title>Top Quotes</title>
<link rel="stylesheet" href="https://fonts.googleapis.com/css2?family=Arimo:wght@400;700&display=swap">
<style>
  :root {
    --navy: #022f63;
    --gold: #f6b80f;
    --nav-ink: #1d2b45;
    --page: #f3f4f6;
    --row: #f0f0f0;
    --row-edge: #e2e2e2;
    --name: #1f6eaf;
    --ink: #111111;
    --white: #ffffff;
  }
  * { box-sizing: border-box; margin: 0; padding: 0; }
  html, body { width: 800px; height: 1200px; overflow: hidden; background: var(--page); }
  .poster {
    width: 700px; height: 1050px;
    transform: scale(1.142857); transform-origin: 0 0;
    position: relative;
    background: linear-gradient(180deg, #f1f2f5 0%, #ffffff 50%, #f1f2f5 100%);
    font-family: "Arimo", Arial, sans-serif;
    color: var(--ink);
  }
  .masthead {
    height: 114px; background: var(--navy);
    display: flex; align-items: center; justify-content: center;
  }
  .masthead-title {
    font-family: "Arimo", Arial, sans-serif;
    font-weight: 700; font-size: 52px; color: var(--white);
    margin-top: -4px;
  }
  .topnav {
    height: 21px; background: var(--gold);
    display: flex; align-items: center; padding-left: 39px; gap: 6.5px;
    font-size: 9.6px; color: var(--nav-ink);
  }
  .section-head {
    position: absolute; top: 150px; left: 39px;
    display: flex; align-items: baseline; gap: 31px;
  }
  .section-title { font-weight: 700; font-size: 17px; }
  .view-all { font-size: 12px; color: var(--name); }
  .quote-list {
    position: absolute; top: 175px; left: 40px; width: 621px;
    list-style: none; display: flex; flex-direction: column; gap: 4px;
  }
  .quote-row {
    height: 104.5px; background: var(--row);
    border-bottom: 1px solid var(--row-edge);
    display: flex; align-items: center;
  }
  .portrait {
    flex: none; width: 78px; height: 98px; margin-left: 7px;
    background: var(--white); padding: 2px;
  }
  .portrait-fill { width: 100%; height: 100%; background: linear-gradient(160deg, #9a9a9a, #3a3a3a); }
  .portrait-fill.light { background: linear-gradient(180deg, #f2f2f2, #d4d4d4); }
  .portrait-fill.silhouette { background: linear-gradient(180deg, #eeeeee 0%, #d8d8d8 55%, #1a1a1a 56%, #111111 100%); }
  .quote-text {
    margin-left: 44px; padding-right: 8px;
    font-size: 14px; line-height: 18px;
  }
  .quote-name { font-weight: 700; font-size: 19px; color: var(--name); }
  .footer {
    position: absolute; left: 0; top: 972px; width: 700px; height: 78px;
    background: var(--navy); color: var(--white);
    display: flex; align-items: center; justify-content: center;
    font-weight: 700; font-size: 13.5px;
  }
</style>
</head>
<body>
<div class="poster">
  <header class="masthead"><h1 class="masthead-title">Top Quotes</h1></header>
  <nav class="topnav">
    <span>Top Quotes</span><span>Top Quotes</span><span>Top Quotes</span><span>Top Quotes</span>
    <span>Top Quotes</span><span>Top Quotes</span><span>Top Quotes</span><span>Top Quotes</span>
    <span>Top Quotes</span><span>Top Quotes</span><span>Top Quotes</span>
  </nav>
  <div class="section-head">
    <h2 class="section-title">Top Quotes</h2>
    <span class="view-all">View all &gt;</span>
  </div>
  <ul class="quote-list">
    <li class="quote-row">
      <div class="portrait"><div class="portrait-fill light" role="img" aria-label="Portrait of Tavish Orlanno"></div></div>
      <p class="quote-text"><span class="quote-name">Tavish Orlanno</span> : “Your beliefs become your thoughts,<br>Your thoughts become your words, Your words become your actions,<br>Your actions become your habits, Your habits become your values,<br>Your values become your destiny.”</p>
    </li>
    <li class="quote-row">
      <div class="portrait"><div class="portrait-fill silhouette" role="img" aria-label="Silhouette for an unknown author"></div></div>
      <p class="quote-text"><span class="quote-name">Unknown</span> : "Winners practice until they get it right.<br>Champions practice until they can’t get it wrong!"</p>
    </li>
    <li class="quote-row">
      <div class="portrait"><div class="portrait-fill" role="img" aria-label="Portrait of Leopold Quimsby"></div></div>
      <p class="quote-text"><span class="quote-name">Leopold Quimsby</span> : "Style is the perfection of a point of view."</p>
    </li>
    <li class="quote-row">
      <div class="portrait"><div class="portrait-fill light" role="img" aria-label="Portrait of Sir Edmund Valcourt"></div></div>
      <p class="quote-text"><span class="quote-name">Sir Edmund Valcourt</span> : "My interest in life comes from setting<br>myself huge, apparently unachieveable challenges and trying to rise<br>above them."</p>
    </li>
    <li class="quote-row">
      <div class="portrait"><div class="portrait-fill" role="img" aria-label="Portrait of Bertram Holloway"></div></div>
      <p class="quote-text"><span class="quote-name">Bertram Holloway</span> : "Problems cannot be solved by the same<br>level of thinking that created them."</p>
    </li>
    <li class="quote-row">
      <div class="portrait"><div class="portrait-fill light" role="img" aria-label="Portrait of Dale Morcum"></div></div>
      <p class="quote-text"><span class="quote-name">Dale Morcum</span> : "People think focus means saying yes to the thing<br>you've got to focus on. But that's not what it means at all. It means<br>saying no to the hundred other good ideas that there are. You have<br>to pick carefully."</p>
    </li>
    <li class="quote-row">
      <div class="portrait"><div class="portrait-fill" role="img" aria-label="Portrait of Lucien Fravel"></div></div>
      <p class="quote-text"><span class="quote-name">Lucien Fravel</span> : "Think like a man of action and act like a man<br>of thought."</p>
    </li>
  </ul>
  <footer class="footer">Discover what’s a good words, for a good life</footer>
</div>
</body>
</html>
```